Wovenpage AD Offer - Meditation Sets

We need a set of 3 WP ads designed as an initial project with a view to doing more over time. The ads are for our meditation products and are simply to offer 20%, 50% and 70% OFF (so we can test what works best) - The text should simply be "50% OFF" or "50% OFF Meditation" etc.

The ads will need to be extremely simple, clear, and bold but also well within WP's 20% text rules.

I have provided one picture for use, but can supply anything you see on the website: www.orbenfield.com if you need it. I've also provided our logo file which needs to be used preferably in the upper right corner of the ad.

Target Market(s)

Yoga Mums - 35yrs, Affluent

Industry/Entity Type

Health And Wellness

Requirements
Must have
• Logo in upper right
• Conform to WP's 20% rules
Should not have
• Overly complex or busy creative

```html
<!DOCTYPE html>
<html lang="en">
<head>
<meta charset="utf-8">
<title>Orbenfield – Meditate in Comfort</title>
<link rel="stylesheet" href="https://fonts.googleapis.com/css2?family=Open+Sans:ital,wght@0,400;0,600;1,400&family=Oswald:wght@600&display=swap">
<style>
  :root{
    --brand-blue:#2d5f8b;
    --brand-navy:#1f4e79;
    --deep-blue:#2a5a86;
    --text-blue:#2f5878;
    --cushion-light:#4673a3;
    --cushion-mid:#2f5d8c;
    --cushion-dark:#234b74;
    --sky:#dbe9f0;
    --mist:#f4f8f7;
    --white:#ffffff;
    --ring:#d7dcdf;
  }
  *{margin:0;padding:0;box-sizing:border-box}
  html,body{width:1200px;height:457px;overflow:hidden;background:var(--white)}
  .ad{
    position:relative;width:1200px;height:457px;overflow:hidden;
    font-family:"Open Sans",Arial,sans-serif;
    background:
      radial-gradient(ellipse 260px 140px at 900px 40px, rgba(58,120,160,.55), transparent 70%),
      radial-gradient(ellipse 320px 120px at 1050px 10px, rgba(40,100,150,.45), transparent 75%),
      radial-gradient(ellipse 420px 220px at 980px 220px, rgba(190,220,225,.7), transparent 70%),
      linear-gradient(100deg, var(--white) 0%, var(--mist) 45%, var(--sky) 100%);
  }
  .product-shot{
    position:absolute;left:22px;top:48px;width:720px;height:388px;
    border-radius:48px;
    background:
      radial-gradient(ellipse 200px 110px at 430px 95px, var(--cushion-light), transparent 75%),
      linear-gradient(160deg, var(--cushion-light) 0%, var(--cushion-mid) 50%, var(--cushion-dark) 100%);
    box-shadow:0 6px 18px rgba(20,50,80,.25);
  }
  .swatches{position:absolute;left:14px;top:430px;display:flex;gap:1px}
  .swatches span{width:12px;height:11px;display:block}
  .brand-badge{
    position:absolute;left:959px;top:-56px;width:256px;height:256px;border-radius:50%;
    background:var(--white);border:5px solid var(--ring);
    box-shadow:0 3px 10px rgba(0,0,0,.25);
  }
  .brand-name{
    position:absolute;left:0;right:18px;top:166px;text-align:center;
    color:var(--brand-blue);font-weight:600;font-size:24px;letter-spacing:2px;
  }
  .offer-badge{
    position:absolute;left:460px;top:258px;width:300px;height:300px;border-radius:50%;
    background:var(--deep-blue);border:8px solid var(--white);
    box-shadow:0 2px 8px rgba(0,0,0,.2);
    color:var(--white);font-family:"Oswald","Arial Narrow",sans-serif;font-weight:600;
  }
  .offer-value{
    position:absolute;left:30px;top:8px;font-size:168px;line-height:1;
    transform:scaleX(.78);transform-origin:left top;letter-spacing:-2px;
  }
  .offer-percent{position:absolute;left:160px;top:16px;font-size:82px;line-height:1}
  .offer-off{position:absolute;left:160px;top:88px;font-size:72px;line-height:1;transform:scaleX(.8);transform-origin:left top}
  .headline{
    position:absolute;left:822px;top:314px;
    color:var(--text-blue);font-size:28px;font-weight:400;letter-spacing:1.3px;white-space:nowrap;
  }
  .tagline{
    position:absolute;left:800px;top:372px;width:400px;height:51px;
    background:var(--brand-navy);
    clip-path:polygon(14px 0,100% 0,100% 100%,0 100%);
    color:var(--white);font-style:italic;font-size:27px;white-space:nowrap;
    display:flex;align-items:center;padding-left:36px;
  }
</style>
</head>
<body>
<main class="ad">
  <div class="product-shot" role="img" aria-label="Photo of a blue meditation floor pillow with a crescent cushion resting on top"></div>

  <div class="swatches" aria-label="Available colours">
    <span style="background:#d42a2a"></span><span style="background:#e04a3a"></span>
    <span style="background:#e8d84a"></span><span style="background:#9aa55a"></span>
    <span style="background:#6f8a4a"></span><span style="background:#2f6f78"></span>
    <span style="background:#2b4f86"></span><span style="background:#1d2f55"></span>
    <span style="background:#7a4f8c"></span><span style="background:#b06aa0"></span>
    <span style="background:#6a4a3a"></span><span style="background:#2a2a2a"></span>
    <span style="background:#e8e4d8"></span>
  </div>

  <div class="brand-badge"><span class="brand-name">ORBENFIELD</span></div>

  <div class="offer-badge" aria-label="20% off">
    <span class="offer-value">20</span>
    <span class="offer-percent">%</span>
    <span class="offer-off">OFF</span>
  </div>

  <h1 class="headline">MEDITATE IN COMFORT</h1>
  <p class="tagline">Are you sitting comfortably?</p>
</main>
</body>
</html>
```